New Zealand Export company needs business cards

We need new business cards to match our new logo for a company based in New Zealand who deal specifically with the Pacific Islands. We source, consolidate and ship products out of New Zealand to the Pacific Islands. Will attach our old ones and also new logo.
Would like the Islands we deal with and the areas of work we have access to, to be included on the business cards.

Contact Information for Business Card

T +64 9 571 3048
F +64 9 571 6285
12-18 Kowhai Lane, Drury, 2113
PO Box 814, Drury, Auckland 2247, New Zealand
www.falconfreight.example.nz
E sales@falconfreight.example.nz

Font styles to use
Sans Serif

Colors
85abd2
33a6d7
ffffff

Requirements
Must have
• A company of PWM

```html
<!DOCTYPE html>
<html lang="en">
<head>
<meta charset="utf-8">
<title>Falcon Freight — Business Card</title>
<link rel="stylesheet" href="https://fonts.googleapis.com/css2?family=Open+Sans:wght@400;700&display=swap">
<style>
  :root {
    --backdrop: #9c9c9c;
    --brand-blue: #0a58a3;
    --brand-sky: #3dbde8;
    --paper: #ffffff;
    --ink: #555555;
  }
  * { margin: 0; padding: 0; box-sizing: border-box; }
  html, body {
    width: 1133px; height: 1200px; overflow: hidden;
    background: var(--backdrop);
    font-family: "Open Sans", Arial, sans-serif;
  }
  .canvas { position: relative; width: 1133px; height: 1200px; }
  .card { position: absolute; left: 219px; width: 694px; height: 397px; }
  .card--front { top: 153px; background: var(--brand-blue); }
  .card--back { top: 649px; background: var(--paper); }

  .wordmark {
    position: absolute; display: flex; align-items: center; gap: 16px;
    font-weight: 700; white-space: nowrap; letter-spacing: 0.5px; line-height: 1;
  }
  .wordmark__square { display: block; flex: none; background: var(--brand-sky); }
  .card--front .wordmark {
    left: 50%; top: 199px; transform: translate(-50%, -50%);
    color: var(--paper); font-size: 50px;
  }
  .card--front .wordmark__square { width: 56px; height: 56px; }
  .card--back .wordmark {
    left: 47px; top: 199px; transform: translateY(-50%);
    color: var(--brand-blue); font-size: 35px; gap: 14px;
  }
  .card--back .wordmark__square { width: 40px; height: 40px; }

  .divider {
    position: absolute; left: 357px; top: 108px; width: 2px; height: 181px;
    background: var(--brand-sky);
  }
  .contact {
    position: absolute; left: 378px; top: 104px;
    color: var(--ink); font-size: 19px; line-height: 25px;
  }
  .contact__address { margin-bottom: 13px; }
  .contact__list { list-style: none; }
  .contact__item { display: flex; align-items: center; gap: 6px; }
  .contact__icon { width: 16px; height: 16px; fill: var(--brand-blue); flex: none; }
</style>
</head>
<body>
<main class="canvas">
  <section class="card card--front" aria-label="Card front">
    <div class="wordmark"><span class="wordmark__square"></span>Falcon Freight</div>
  </section>

  <section class="card card--back" aria-label="Card back">
    <div class="wordmark"><span class="wordmark__square"></span>Falcon Freight</div>
    <div class="divider"></div>
    <div class="contact">
      <p class="contact__address">12-18 Kowhai Lane, Drury, 2113<br>PO Box 814, Drury<br>Auckland 2247, New Zealand</p>
      <ul class="contact__list">
        <li class="contact__item">
          <svg class="contact__icon" viewBox="0 0 16 16" aria-hidden="true"><path d="M3.6 1.2l2.2 2.8-1.3 1.7c.9 2 2.6 3.7 4.6 4.6l1.7-1.3 2.8 2.2-1.5 2.6C7.2 13.6 2.4 8.8 1.1 2.9z"/></svg>
          <span>+64 9 571 3048</span>
        </li>
        <li class="contact__item">
          <svg class="contact__icon" viewBox="0 0 16 16" aria-hidden="true"><path d="M4 1h8v4H4zM1 6h14v6h-3v3H4v-3H1zm4 4v4h6v-4z"/></svg>
          <span>+64 9 571 6285</span>
        </li>
        <li class="contact__item">
          <svg class="contact__icon" viewBox="0 0 16 16" aria-hidden="true"><path d="M1 3h14v1.5L8 9 1 4.5zm0 3.3L8 11l7-4.7V13H1z"/></svg>
          <span>sales@falconfreight.example.nz</span>
        </li>
        <li class="contact__item">
          <svg class="contact__icon" viewBox="0 0 16 16" aria-hidden="true"><circle cx="8" cy="8" r="7"/></svg>
          <span>www.falconfreight.example.nz</span>
        </li>
      </ul>
    </div>
  </section>
</main>
</body>
</html>
```